依頼詳細
キャッチコピーは以下になります。変わる可能性がありますので文字修正は簡単にできるようにお願いします。
PSDファイル、高解像度JPG、PNG形式、全てのファイル納品でお願いいたします。
記載項目
テキストにつきましては、
添付資料に記載をさせて頂いております。

また前回のコンペの当選したデザインを
参考に添付させて頂いておりますので、

もしよろしければご参照くださいませ。

当社、
ABテストを繰り返し実施しておりますので、
当選のデザインを複数選ばせて頂いております。

2020年11月29日 当選デザイン 5つ
2020年12月07日 当選デザイン 4つ
2020年12月07日 当選デザイン 8つ

普段のコンペよりも当選の確率がかなり高いので、
ぜひご参加して頂けると幸いでございます。

コンペ終了後は当選の方が
納品完了後に当選の手続きになりますので、

当選の方はお早めに納品をして頂けますと
助かりますのでどうぞよろしくお願い致します。

--------------------------------------------------------

今回のデザインでございますが、

右上の部分は書籍・教材のイメージで作成をして頂きたいです。

デザイナー様の自由な発想でデザインをお願いします。

どうぞよろしくお願い致します。
サイズ
• 2001(縦) x 1125(横)
希望イメージ
シンプル 複雑
単色 カラフル
暗い 明るい
日常 高級
遊び心 厳粛
未来的 伝統的
女性的 男性的
希望する色
納品ファイル
• 高解像度JPG (.jpg)
• フォトショップ形式 (.psd)
• PNG形式 (.png)
補足説明
<ターゲット>
40代 男性

<その他>
当LPを閲覧する人の80%程度はスマホでの閲覧と想定されます。
スマホで閲覧しても、当選した後に別途追加1,000円程度でPCからの閲覧でも
きれいに表示されるように縦957px×横1300pxでサイズ修正をお願いいたします。

<継続依頼>
当選者様にはそのままヘッダー以下のデザインもお願いしたいと思っています。
また本案件のコピー以外のパターンのデザインも追加発注も考えております。
価格についてはまたご相談させて頂きます。
前回の当選したデザインを追加します。

参考になりましたら幸いでございます。
積立式ネット物販.pngのデザインをどうぞよろしくお願いします。
田舎ネット物販.pdfは前回当選したデザインになります。
改めてのご連絡になります。
写真のサイスは
2001(縦) x 1125(横)になりますので、
どうぞよろしくお願いします。
■ 選んだ理由

安心感・信頼感あるデザイン
シンプルなデザイン
を選ばせて頂きました。

■ 提案者全員のお礼・コメント

当社のコンペに参加して頂きありがとうございました。

来年もコンペを開催させて頂きますので、どうぞよろしくお願い致します。

```html
<!DOCTYPE html>
<html lang="ja">
<head>
<meta charset="UTF-8">
<title>手堅い 積立式ネット物販</title>
<link href="https://fonts.googleapis.com/css2?family=Noto+Sans+JP:wght@400;500;700;900&display=swap" rel="stylesheet">
<style>
:root{
  --navy:#0b1f4d;
  --navy-deep:#071638;
  --blue:#1a5fb4;
  --blue-bright:#2d8be0;
  --sky:#e8f3fb;
  --line-blue:#9cc9ea;
  --green:#2fbf3a;
  --green-dark:#1f9a2a;
  --green-light:#8ee04a;
  --white:#ffffff;
  --ink:#14254f;
  --gray:#555;
}
*{margin:0;padding:0;box-sizing:border-box}
html,body{width:673px;height:1200px;overflow:hidden}
body{font-family:"Noto Sans JP",sans-serif;background:var(--white);color:var(--ink)}
.banner{position:relative;width:673px;height:1200px;overflow:hidden;
  background:linear-gradient(180deg,var(--sky) 0%,#ffffff 100%)}
.hero{position:absolute;left:0;top:0;width:673px;height:690px;
  background:linear-gradient(160deg,#0e2d6b 0%,#123f8f 45%,#0a2561 100%)}
.top-strip{position:absolute;left:0;top:0;width:673px;height:40px;background:var(--navy-deep);
  color:var(--white);font-weight:700;font-size:21px;text-align:center;line-height:40px;letter-spacing:1px;z-index:3}
.photo{position:absolute;left:300px;top:40px;width:373px;height:460px;
  background:linear-gradient(135deg,#3d6fb8 0%,#1b3d7c 50%,#0d2657 100%)}
.tagline-box{position:absolute;left:88px;top:50px;width:140px;height:42px;background:var(--white);
  color:var(--navy);font-weight:900;font-size:28px;text-align:center;line-height:42px;letter-spacing:2px;z-index:2}
.title{position:absolute;left:0;top:0;width:340px;height:300px;z-index:2;font-weight:900;color:var(--green-light);
  text-shadow:0 3px 6px rgba(0,0,0,.45)}
.title span{display:block;position:absolute;line-height:1;white-space:nowrap}
.title-vertical{left:44px;top:122px;width:50px;font-size:44px;text-align:center}
.title-vertical i{display:block;font-style:normal;height:44px}
.title-net{left:100px;top:112px;font-size:72px;letter-spacing:-2px}
.title-main{left:104px;top:182px;font-size:100px;letter-spacing:4px}
.points{position:absolute;left:36px;top:314px;list-style:none;z-index:2}
.points li{display:flex;align-items:center;gap:10px;color:var(--white);font-weight:700;font-size:25px;height:38px;margin-bottom:4px;text-shadow:0 2px 4px rgba(0,0,0,.5)}
.points svg{width:28px;height:28px;flex:none}
.book{position:absolute;left:40px;top:450px;width:245px;height:225px;z-index:2;
  background:linear-gradient(160deg,#f4f8fc 0%,#cfe0f2 60%,#2f6fbf 100%);border-radius:4px;
  box-shadow:0 6px 14px rgba(0,0,0,.35)}
.offer{position:absolute;left:296px;top:515px;width:370px;text-align:center;color:var(--white);font-weight:900;z-index:2;
  text-shadow:0 3px 6px rgba(0,0,0,.5)}
.offer p{font-size:42px;line-height:54px;letter-spacing:1px}
.cta-lead{position:absolute;left:0;top:690px;width:673px;text-align:center;z-index:2}
.cta-lead .brand-line{display:flex;justify-content:center;align-items:center;gap:8px;font-weight:900;font-size:36px;color:var(--navy);line-height:48px}
.cta-lead .brand{color:var(--green)}
.cta-lead .sub{font-weight:900;font-size:34px;color:var(--navy);line-height:46px;letter-spacing:1px}
.perks{position:absolute;left:18px;top:800px;width:637px;list-style:none}
.perk{display:flex;height:76px;margin-bottom:10px;background:var(--white);border:2px solid var(--line-blue)}
.perk-tag{width:62px;flex:none;background:var(--blue);color:var(--white);display:flex;flex-direction:column;
  align-items:center;justify-content:center;font-weight:700;font-size:15px;line-height:1.1}
.perk-tag b{font-size:30px;font-weight:900}
.perk-icon{width:70px;flex:none;display:flex;align-items:center;justify-content:center}
.perk-icon svg{width:46px;height:46px}
.perk-text{display:flex;flex-direction:column;justify-content:center;font-weight:700}
.perk-text .l1{font-size:22px;color:var(--blue)}
.perk-text .l2{font-size:23px;color:var(--navy);font-weight:900;border-bottom:2px solid var(--navy);align-self:flex-start;line-height:1.2}
.button{position:absolute;left:18px;top:1062px;width:637px;height:62px;border-radius:10px;
  background:linear-gradient(180deg,#4dd655 0%,var(--green-dark) 100%);box-shadow:0 4px 0 #157a1e;
  color:var(--white);font-weight:900;font-size:30px;display:flex;align-items:center;justify-content:center;gap:14px;letter-spacing:1px}
.button svg{width:34px;height:34px}
.footer-links{position:absolute;left:0;top:1140px;width:673px;text-align:center;font-size:18px;color:var(--gray)}
.footer-links span{margin:0 10px}
</style>
</head>
<body>
<div class="banner">
  <div class="hero"></div>
  <div class="top-strip">今日から将来に向けて資産構築をしたいあなたに</div>
  <div class="photo" role="img" aria-label="スーツ姿のビジネスマンの写真"></div>

  <div class="tagline-box">手堅い</div>
  <h1 class="title">
    <span class="title-vertical"><i>積</i><i>立</i><i>式</i></span>
    <span class="title-net">ネット</span>
    <span class="title-main">物販</span>
  </h1>

  <ul class="points">
    <li><svg viewBox="0 0 28 28"><path d="M14 3 L24 8 V16 L14 26 Z" fill="#2fbf3a"/><path d="M14 3 L4 8 V16 L14 26 Z" fill="#f6d31c"/></svg>初心者におすすめの副業</li>
    <li><svg viewBox="0 0 28 28"><rect x="3" y="18" width="5" height="7" fill="#2d8be0"/><rect x="11" y="13" width="5" height="12" fill="#2d8be0"/><rect x="19" y="8" width="5" height="17" fill="#2d8be0"/><path d="M3 14 L12 7 L17 10 L25 3" stroke="#f6d31c" stroke-width="2.5" fill="none"/></svg>毎週収入が積み上がる</li>
    <li><svg viewBox="0 0 28 28"><circle cx="14" cy="16" r="10" fill="#e3a82b"/><path d="M10 4 H18 L16 8 H12 Z" fill="#e3a82b"/><text x="14" y="21" font-size="12" font-weight="900" text-anchor="middle" fill="#fff" font-family="sans-serif">¥</text></svg>初期費用がかからない</li>
  </ul>

  <div class="book" role="img" aria-label="初心者でもわかる積立式物販の教科書スタートマニュアルの冊子イメージ"></div>

  <div class="offer">
    <p>豪華３大特典を</p>
    <p>今だけ300部限定</p>
    <p>無料！！</p>
  </div>

  <div class="cta-lead">
    <div class="brand-line">
      <svg width="34" height="34" viewBox="0 0 34 34"><rect x="3" y="12" width="28" height="8" fill="#2fbf3a"/><rect x="5" y="20" width="24" height="12" fill="#2fbf3a"/><rect x="15" y="12" width="4" height="20" fill="#f6d31c"/><path d="M17 12 C12 4 7 8 17 12 C27 8 22 4 17 12" stroke="#f6d31c" stroke-width="2.5" fill="none"/></svg>
      <span><span class="brand">TALKY追加</span>で</span>
    </div>
    <p class="sub">今日から始められる特典をプレゼント</p>
  </div>

  <ul class="perks">
    <li class="perk">
      <div class="perk-tag">特典<b>1</b></div>
      <div class="perk-icon"><svg viewBox="0 0 46 46"><path d="M4 10 Q14 6 23 11 Q32 6 42 10 V38 Q32 34 23 39 Q14 34 4 38 Z" fill="none" stroke="#14254f" stroke-width="3"/><line x1="23" y1="11" x2="23" y2="39" stroke="#14254f" stroke-width="3"/></svg></div>
      <div class="perk-text"><span class="l1">ネット物販がゼロからわかる</span><span class="l2">マル秘マニュアル</span></div>
    </li>
    <li class="perk">
      <div class="perk-tag">特典<b>2</b></div>
      <div class="perk-icon"><svg viewBox="0 0 46 46"><rect x="4" y="6" width="38" height="26" fill="none" stroke="#14254f" stroke-width="3"/><path d="M19 13 L29 19 L19 25 Z" fill="#14254f"/><line x1="23" y1="32" x2="23" y2="40" stroke="#14254f" stroke-width="3"/><line x1="14" y1="40" x2="32" y2="40" stroke="#14254f" stroke-width="3"/></svg></div>
      <div class="perk-text"><span class="l1">積立式ネット物販がゼロからわかる</span><span class="l2">ノウハウと講座の動画４本</span></div>
    </li>
    <li class="perk">
      <div class="perk-tag">特典<b>3</b></div>
      <div class="perk-icon"><svg viewBox="0 0 46 46"><rect x="8" y="4" width="30" height="38" fill="none" stroke="#14254f" stroke-width="3"/><line x1="14" y1="14" x2="32" y2="14" stroke="#14254f" stroke-width="3"/><line x1="14" y1="22" x2="32" y2="22" stroke="#14254f" stroke-width="3"/><line x1="14" y1="30" x2="32" y2="30" stroke="#14254f" stroke-width="3"/></svg></div>
      <div class="perk-text"><span class="l1">積立式ネット物販で売れた</span><span class="l2">高額商品リスト</span></div>
    </li>
  </ul>

  <div class="button">TALKY追加で特典を受けとる
    <svg viewBox="0 0 34 34"><circle cx="17" cy="17" r="16" fill="#fff"/><path d="M13 10 L24 17 L13 24 Z" fill="#1f9a2a"/></svg>
  </div>

  <div class="footer-links"><span>特商法</span><span>プライバシーポリシー</span></div>
</div>
</body>
</html>
```